TV Media buying firm needs Lead Gen page layout

We need a landing page using our current website look and feel to capture leads from our Chatterleaf ads. A quick form to capture Name, phone number, email, and a short message.
The call to action button should state "Get a free direct response campaign audit now!"
Updates

please visit www.brantlowmedia.com for the look and feel of the landing page.

I also uploaded a screenshot of what kind of landing page we are looking for.
the image has been reduced to 50% for the overall view.
thanks!

Please use our website's look and feel as reference for colors, fonts,header and footers.

The video placement on the sample file can be an image or combination image & text.

Again, please reference www.brantlowmedia.com for the look and feel.

Target Market(s)

50+ Market, Cheif Marketing Officer, Summit 1000 Companies

Industry/Entity Type

Tv

```html
<!DOCTYPE html>
<html lang="en">
<head>
<meta charset="utf-8">
<title>Brantlow Media – Lead Capture</title>
<link href="https://fonts.googleapis.com/css2?family=Arimo:wght@400;700&family=PT+Sans+Narrow:wght@400;700&display=swap" rel="stylesheet">
<style>
:root{
  --red:#d71f26;
  --red-dark:#a5141a;
  --ink:#222;
  --text:#555;
  --footer-top:#5a5a5a;
  --footer-bottom:#1f1f1f;
  --field-border:#c9c9c9;
}
*{box-sizing:border-box;margin:0;padding:0}
html,body{width:865px;height:1200px;overflow:hidden;background:#fff}
body{position:relative;font-family:"Arimo",Arial,sans-serif;color:var(--text)}
.title-bar{position:absolute;left:0;top:0;width:865px;height:26px;
  background:repeating-linear-gradient(135deg,#3a3a3a 0 2px,#2a2a2a 2px 4px);
  color:#eee;font-size:11px;line-height:26px;padding-left:12px}
.site-header{position:absolute;left:0;top:26px;width:865px;height:109px;
  background:linear-gradient(#f4f4f4,#fff)}
.brand{position:absolute;left:22px;top:32px}
.brand-name{font-family:"Arimo",Arial,sans-serif;font-weight:700;font-size:36px;color:var(--ink);line-height:1}
.brand-tag{font-size:10px;color:#555;margin-top:5px;letter-spacing:.4px}
.contact{position:absolute;right:18px;top:26px;text-align:right}
.contact-label{font-weight:700;font-size:16px;color:var(--ink);display:flex;align-items:center;justify-content:flex-end;gap:6px}
.contact-phone{font-weight:700;font-size:27px;color:var(--red);margin-top:4px;letter-spacing:.5px}
.hero{position:absolute;left:0;top:135px;width:865px;height:342px;
  background:linear-gradient(var(--red),var(--red-dark))}
.hero-photo{position:absolute;left:35px;top:25px;width:449px;height:289px;border:2px solid #111;
  background:radial-gradient(ellipse at 60% 40%,#6b6b6b,#1c1c1c 75%)}
.lead-form{position:absolute;left:546px;top:22px;width:267px;height:296px;background:#fff}
.form-head{position:absolute;left:-7px;top:9px;width:281px;height:48px;background:#262626;color:#fff;
  font-family:"PT Sans Narrow",sans-serif;font-weight:700;font-size:22px;text-align:center;line-height:48px}
.form-head::before,.form-head::after{content:"";position:absolute;bottom:-7px;border-top:7px solid #111}
.form-head::before{left:0;border-left:7px solid transparent}
.form-head::after{right:0;border-right:7px solid transparent}
.field{position:absolute;left:47px;width:207px;height:26px;border:1px solid var(--field-border);
  font-size:13px;color:#999;padding:5px 4px}
.field-icon{position:absolute;left:11px;width:27px;height:27px;border-radius:50%;background:#c8c8c8}
.cta{position:absolute;left:47px;top:245px;width:207px;height:39px;background:var(--red-dark);color:#fff;
  font-family:"PT Sans Narrow",sans-serif;font-weight:700;font-size:12.5px;text-align:center;line-height:15px;padding-top:4px}
.client-band{position:absolute;left:0;top:477px;width:865px;height:93px;
  background:linear-gradient(#d8d8d8,#f3f3f3);display:flex;align-items:center;justify-content:space-around;padding:0 30px}
.client{font-weight:700;font-size:17px;color:#666;display:flex;align-items:center;gap:6px}
.client i{display:block;width:14px;height:14px;background:#777}
.section-title{position:absolute;left:0;top:610px;width:865px;text-align:center;
  font-family:"PT Sans Narrow",sans-serif;font-weight:700;font-size:42px;color:#444}
.service{position:absolute;width:400px}
.service-icon{position:absolute;left:0;top:0;width:96px;height:96px;border-radius:50%;
  background:radial-gradient(circle at 40% 30%,#ef3a3f,#b3141a)}
.service-icon svg{position:absolute;left:24px;top:24px}
.service-title{position:absolute;left:110px;top:0;width:251px;border-bottom:1px solid #bbb;height:28px;
  font-family:"PT Sans Narrow",sans-serif;font-weight:700;font-size:22px;color:var(--ink);line-height:24px}
.service-title span{position:absolute;right:0;top:9px;font-family:"Arimo",sans-serif;font-size:11px;color:var(--red)}
.service p{position:absolute;left:110px;top:38px;width:272px;font-size:12.6px;line-height:15px}
.site-footer{position:absolute;left:0;top:1042px;width:865px;height:158px;
  background:linear-gradient(var(--footer-top),var(--footer-bottom));color:#ddd;text-align:center}
.footer-links{font-size:10.6px;line-height:12.6px;padding-top:36px}
.footer-note{font-size:12.5px;color:#fff;margin-top:18px}
</style>
</head>
<body>
<div class="title-bar">DRTV, Media Buying, Direct Response Television, DRTV Advertising, World Class Media Buying Agency - Brantlow Media</div>

<header class="site-header">
  <div class="brand">
    <div class="brand-name">Brantlow Media</div>
    <div class="brand-tag">INTEGRATED RESPONSE MEDIA</div>
  </div>
  <div class="contact">
    <div class="contact-label">
      <svg width="22" height="22" viewBox="0 0 22 22"><circle cx="11" cy="11" r="10" fill="none" stroke="#222" stroke-width="1.6"/><path d="M7.5 6.5l2 2-1 1.3c.6 1.3 1.5 2.2 2.8 2.8l1.3-1 2 2-1.2 1.6c-3.5-.5-6.6-3.6-7.1-7.1z" fill="#222"/></svg>
      Contact us
    </div>
    <div class="contact-phone">555.214.3870</div>
  </div>
</header>

<section class="hero">
  <div class="hero-photo" role="img" aria-label="Photo of the agency's two founders standing before a wall of studio monitors"></div>
  <form class="lead-form">
    <div class="form-head">Drive Your Business Growth</div>
    <i class="field-icon" style="top:70px"></i><div class="field" style="top:70px">Name *</div>
    <i class="field-icon" style="top:105px"></i><div class="field" style="top:105px">Email *</div>
    <i class="field-icon" style="top:140px"></i><div class="field" style="top:140px">Phone *</div>
    <i class="field-icon" style="top:176px"></i><div class="field" style="top:176px;height:62px">Short Message *</div>
    <div class="cta">GET A FREE DIRECT RESPONSE<br>CAMPAIGN AUDIT NOW!</div>
  </form>
</section>

<div class="client-band">
  <div class="client"><i></i>Skyreach</div>
  <div class="client">VitaPage</div>
  <div class="client">Hollis &amp; Crane</div>
  <div class="client">QuickLedger</div>
  <div class="client">RateHarbor</div>
  <div class="client"><i style="border-radius:50%"></i>WallGiant</div>
</div>

<h1 class="section-title">Direct Response Marketing Agency: What We Do</h1>

<div class="service" style="left:32px;top:715px">
  <div class="service-icon"><svg width="48" height="48" viewBox="0 0 48 48"><rect x="3" y="8" width="42" height="32" rx="3" fill="none" stroke="#fff" stroke-width="3"/><circle cx="24" cy="24" r="8" fill="none" stroke="#fff" stroke-width="2.5"/><path d="M21 19.5l7 4.5-7 4.5z" fill="#fff"/></svg></div>
  <h2 class="service-title">Media Buying Experts<span>more +</span></h2>
  <p>One company in the direct response television industry is leading the charge to provide clients with an integrated, multi-channel direct response media buying strategy. That company is Brantlow Media</p>
</div>

<div class="service" style="left:455px;top:715px">
  <div class="service-icon"><svg width="48" height="48" viewBox="0 0 48 48"><path d="M24 4c-7 0-12 5-12 12 0 9 12 20 12 20s12-11 12-20c0-7-5-12-12-12z" fill="none" stroke="#fff" stroke-width="3"/><circle cx="24" cy="16" r="4.5" fill="#fff"/><path d="M6 40h36" stroke="#fff" stroke-width="3"/></svg></div>
  <h2 class="service-title">TRACE Technology<span>more +</span></h2>
  <p>Brantlow Media has developed a sophisticated audience profiling and tracking platform (TRACE). This new technology enables us to more efficiently reach the right target customer for each direct response campaign.</p>
</div>

<div class="service" style="left:32px;top:892px">
  <div class="service-icon"><svg width="48" height="48" viewBox="0 0 48 48"><rect x="4" y="8" width="40" height="26" rx="2" fill="none" stroke="#fff" stroke-width="3"/><path d="M18 42h12M24 34v8" stroke="#fff" stroke-width="3"/></svg></div>
  <h2 class="service-title">Online Integration<span>more +</span></h2>
  <p>With an infomercial campaign that incorporates an online marketing component you can reach a broader customer base than just using a traditional DRTV campaign without an Internet presence.</p>
</div>

<div class="service" style="left:455px;top:892px">
  <div class="service-icon"><svg width="48" height="48" viewBox="0 0 48 48"><rect x="4" y="16" width="40" height="20" rx="10" fill="none" stroke="#fff" stroke-width="3"/><path d="M14 22v8M10 26h8" stroke="#fff" stroke-width="3"/><circle cx="32" cy="24" r="2.2" fill="#fff"/><circle cx="37" cy="28" r="2.2" fill="#fff"/></svg></div>
  <h2 class="service-title">Multi-Channel<span>more +</span></h2>
  <p>Did you know that TV drives consumers to search more than any other medium? And 39% of online searches influenced by offline media , like TV, make a purchase.</p>
</div>

<footer class="site-footer">
  <div class="footer-links">
    drtv home | about us | key management | services | direct response television | drtv infomercial | online direct response | radio direct response<br>
    print direct response | drtv lead generation | branded drtv | senior marketing specialist | media buying services | television media buying<br>
    media buyer planning | reporting &amp; analysis | case studies | resources | client portfolio | past articles | contact us | site map<br>
    Brantlow Interactive | Integrated Response Media | Infomercial
  </div>
  <div class="footer-note">Integrated Response Media is a trademark of Brantlow, Brantlow Media and Brantlow Interactive.</div>
</footer>
</body>
</html>
```